front and back labels on a single sheet.

Vodka label design
Vodka is a colourless liquor. This vodka is tasteless and with no flavour.

FRONT LABEL
"FROST TALLY" is the brand name . it should be as big as possible.
below that " Only vodka made from sustainable means"
Remaining details to be copied from attached file.
Back Label
Details attached.

Colors
00AB8E
00BBA5
67D7C9
C6EFE9
E9F9F6

```html
<!DOCTYPE html>
<html lang="en">
<head>
<meta charset="utf-8">
<title>Frost Tally Vodka – Front and Back Labels</title>
<link href="https://fonts.googleapis.com/css2?family=Bebas+Neue&family=Montserrat:wght@300;400;500;600;700&family=Oswald:wght@400;500&display=swap" rel="stylesheet">
<style>
  :root {
    --sheet: #e6d9a6;
    --label: #ffffff;
    --ink: #111111;
    --ink-soft: #3a3a3a;
    --grey-line: #8a8a8a;
    --texture-top: #d9dbdd;
    --texture-fade: #ffffff;
    --brand-green: #2e8b2e;
    --warning-red: #d4141c;
  }
  * { box-sizing: border-box; margin: 0; padding: 0; }
  html, body { width: 1200px; height: 1181px; overflow: hidden; }
  body {
    background: var(--sheet);
    font-family: "Montserrat", sans-serif;
    color: var(--ink);
    position: relative;
  }
  .label {
    position: absolute;
    top: 250px;
    width: 470px;
    height: 680px;
    background: var(--label);
    overflow: hidden;
  }
  .label--front { left: 80px; }
  .label--back { left: 650px; }
  .texture {
    position: absolute;
    left: 0; top: 0;
    width: 100%;
    height: 300px;
    background: linear-gradient(180deg, var(--texture-top) 0%, #eceeef 45%, var(--texture-fade) 100%);
  }
  .label--back .texture { height: 260px; }

  /* front */
  .maker {
    position: absolute;
    top: 28px; left: 0; width: 100%;
    text-align: center;
  }
  .maker__row { display: inline-flex; align-items: center; gap: 8px; }
  .maker__dot { width: 16px; height: 16px; border-radius: 50%; background: var(--brand-green); }
  .maker__name { font-weight: 700; font-size: 15px; letter-spacing: 0.5px; color: var(--brand-green); }
  .maker__tagline {
    margin-top: 6px;
    font-size: 5px; font-weight: 600; letter-spacing: 0.3px;
    color: var(--ink-soft);
  }
  .brand-frame {
    position: absolute;
    left: 56px; top: 124px;
    width: 358px; height: 376px;
    border: 4px solid var(--ink);
    background: rgba(255,255,255,0.55);
  }
  .brand-name {
    position: absolute;
    top: 10px; left: 0; width: 100%;
    text-align: center;
    font-family: "Bebas Neue", sans-serif;
    font-weight: 400;
    font-size: 158px;
    line-height: 132px;
    letter-spacing: 1px;
    background: linear-gradient(180deg, #111 0%, #111 48%, #5a5a5a 50%, #1a1a1a 58%, #111 98%);
    -webkit-background-clip: text;
    background-clip: text;
    color: transparent;
  }
  .brand-band {
    position: absolute;
    left: 0; bottom: 0; width: 100%; height: 86px;
    background: var(--ink);
    color: #fff;
    font-family: "Oswald", sans-serif;
    font-weight: 500;
    font-size: 27px;
    line-height: 40px;
    text-align: center;
    padding-top: 3px;
  }
  .brand-band__line { display: flex; align-items: center; justify-content: center; gap: 10px; white-space: nowrap; }
  .brand-band__rule { width: 22px; height: 2px; background: #fff; }
  .quality {
    position: absolute;
    left: 58px; top: 524px; width: 356px;
    border-top: 1.5px solid var(--ink);
    border-bottom: 1.5px solid var(--ink);
    text-align: center;
    white-space: nowrap;
    font-family: "Oswald", sans-serif;
    font-weight: 500;
    font-size: 24px;
    letter-spacing: 3px;
    line-height: 52px;
  }
  .spec {
    position: absolute; top: 608px;
    font-family: "Oswald", sans-serif;
    font-weight: 500; font-size: 30px; letter-spacing: 2px;
    line-height: 40px;
  }
  .spec--abv { left: 22px; }
  .spec--volume { right: 22px; }

  /* back */
  .story {
    position: absolute;
    top: 140px; left: 14px; width: 442px;
    text-align: center;
    font-size: 12.5px; font-weight: 500;
    line-height: 21px;
    text-transform: uppercase;
  }
  .notices {
    position: absolute;
    top: 264px; left: 54px;
    display: flex; align-items: center; gap: 14px;
  }
  .pregnancy {
    display: flex; align-items: center; gap: 8px;
    border: 1.5px solid var(--warning-red);
    border-radius: 6px;
    padding: 4px 16px 4px 0;
    margin-left: 14px;
  }
  .pregnancy__icon { margin-left: -14px; background: #fff; border-radius: 50%; }
  .pregnancy__title { color: var(--warning-red); font-weight: 700; font-size: 11px; letter-spacing: 0.5px; white-space: nowrap; }
  .pregnancy__text { font-size: 10px; line-height: 12px; white-space: nowrap; }
  .standard-drink {
    position: relative;
    width: 62px; height: 76px;
    text-align: center;
    font-weight: 700;
    font-size: 8px; line-height: 9px;
    padding-top: 3px;
  }
  .standard-drink__outline { position: absolute; left: 0; top: 0; }
  .standard-drink__text { position: relative; }
  .standard-drink__count {
    display: block;
    background: var(--ink); color: #fff;
    font-size: 26px; line-height: 28px;
    margin: 2px 5px;
  }
  .standard-drink__approx { font-size: 7px; }
  .recycle { text-align: center; font-size: 9px; font-weight: 700; }
  .info-box {
    position: absolute;
    top: 360px; left: 26px; width: 418px; height: 116px;
    border: 1px solid var(--grey-line);
    display: flex;
    padding: 10px 10px;
  }
  .info-box__col { flex: 1; font-size: 10.5px; line-height: 14px; font-weight: 300; color: var(--ink-soft); text-transform: uppercase; }
  .info-box__col--use { padding-right: 14px; }
  .info-box__col--maker { border-left: 1.5px solid var(--ink); padding-left: 20px; padding-top: 4px; }
  .info-box__contact { font-size: 7.5px; font-weight: 500; line-height: 10px; margin-top: 4px; color: var(--ink); }
  .info-box__origin { font-weight: 600; color: var(--ink); margin-top: 6px; }
  .source {
    position: absolute;
    top: 528px; left: 0; width: 100%;
    text-align: center;
    font-weight: 700; font-size: 20px; letter-spacing: 0.3px;
  }
</style>
</head>
<body>

<section class="label label--front" aria-label="Front label">
  <div class="texture" role="img" aria-label="Soft grey dotted halftone texture fading to white"></div>
  <div class="maker">
    <div class="maker__row">
      <span class="maker__dot"></span>
      <span class="maker__name">VERDANT STILL</span>
    </div>
    <div class="maker__tagline">SPIRITS SHAPED BY QUIET GREEN FIELDS</div>
  </div>
  <div class="brand-frame">
    <h1 class="brand-name">FROST<br>TALLY</h1>
    <div class="brand-band">
      <div class="brand-band__line"><span class="brand-band__rule"></span>ONLY VODKA MADE<span class="brand-band__rule"></span></div>
      <div class="brand-band__line">FROM SUSTAINABLE MEANS</div>
    </div>
  </div>
  <div class="quality">PREMIUM QUALITY VODKA</div>
  <div class="spec spec--abv">50%</div>
  <div class="spec spec--volume">750ml</div>
</section>

<section class="label label--back" aria-label="Back label">
  <div class="texture" role="img" aria-label="Soft grey dotted halftone texture fading to white"></div>
  <p class="story">The only vodka in the whole world which has unique 5 spices, and distilled 3+1 times. In addition this is the only vodka made from natural rainwater &amp; solar power, thus making it the only vodka that is sustainably manufactured.</p>

  <div class="notices">
    <div class="pregnancy">
      <svg class="pregnancy__icon" width="40" height="40" viewBox="0 0 40 40" aria-label="No alcohol during pregnancy">
        <circle cx="20" cy="20" r="17" fill="none" stroke="#d4141c" stroke-width="4"/>
        <line x1="8" y1="8" x2="32" y2="32" stroke="#d4141c" stroke-width="4"/>
      </svg>
      <div>
        <div class="pregnancy__title">PREGNANCY WARNING</div>
        <div class="pregnancy__text">Alcohol can cause lifelong<br>harm to your baby</div>
      </div>
    </div>
    <div class="standard-drink">
      <svg class="standard-drink__outline" width="62" height="76" viewBox="0 0 62 76" aria-hidden="true">
        <path d="M1 1 H61 V63 L31 75 L1 63 Z" fill="#fff" stroke="#111" stroke-width="2" stroke-linejoin="round"/>
      </svg>
      <div class="standard-drink__text">STANDARD<br>DRINK<span class="standard-drink__count">27</span><span class="standard-drink__approx">APPROX.</span></div>
    </div>
    <div class="recycle">
      <svg width="40" height="38" viewBox="0 0 40 38" aria-label="Recyclable">
        <polygon points="20,4 36,32 4,32" fill="none" stroke="#111" stroke-width="3.5" stroke-linejoin="round"/>
        <polygon points="26,4 20,4 23,10" fill="#111"/>
      </svg>
      <div>GLASS</div>
    </div>
  </div>

  <div class="info-box">
    <div class="info-box__col info-box__col--use">
      This vodka has to be taken chilled with ice cubes. Making cocktails with lime and orange is a wonderful experience.
      <div class="info-box__contact">Contact at:<br>contact@verdantstill.example</div>
    </div>
    <div class="info-box__col info-box__col--maker">
      Fermented and distilled by: Marlow J. Penfield at Verdant Still Pvt Ltd
      <div class="info-box__origin">Made in: Halden Creek,<br>Victoria, Australia</div>
    </div>
  </div>

  <div class="source">MADE FROM SUGARCANE</div>
</section>

</body>
</html>
```